Swimming pool service business postcard redesign

We need a fresh post card design for our pool service business based in San Diego called Tide Sweepers. We are a family based, local residential pool cleaning and maintenance company. we need an offer to stand out, our logo, our colors, etc on a 5.5x8 inch full color post card.

```html
<!DOCTYPE html>
<html lang="en">
<head>
<meta charset="utf-8">
<title>Tide Sweepers – Service Agreement Postcard</title>
<link href="https://fonts.googleapis.com/css2?family=Tinos:ital,wght@0,400;0,700;1,400;1,700&display=swap" rel="stylesheet">
<style>
  :root {
    --page-bg: #e6e6e6;
    --card-white: #ffffff;
    --accent-orange: #e26544;
    --heading-orange: #e0603f;
    --ink: #1c1c1c;
    --blue-light: #6fb3e0;
    --blue-mid: #3a8cc4;
    --blue-deep: #1469a3;
    --brand-blue: #1f5c9a;
  }
  * { box-sizing: border-box; margin: 0; padding: 0; }
  html, body { width: 988px; height: 1200px; overflow: hidden; }
  body {
    background: var(--page-bg);
    font-family: "Tinos", "Times New Roman", serif;
    color: var(--ink);
    position: relative;
  }
  .card {
    position: absolute;
    left: 121px;
    width: 745px;
    height: 511px;
    background: var(--card-white);
    overflow: hidden;
    box-shadow: 0 2px 8px rgba(0,0,0,.18);
  }
  .card--front { top: 56px; }
  .card--back { top: 612px; }

  /* Front: brand + service charges */
  .brand {
    position: absolute;
    left: 0; top: 0;
    width: 283px; height: 195px;
    display: flex; align-items: center; justify-content: center; gap: 10px;
  }
  .brand__dot {
    width: 22px; height: 22px; border-radius: 50%;
    background: var(--accent-orange);
    flex: none;
  }
  .brand__name { font-weight: 700; font-size: 28px; color: var(--brand-blue); }

  .charges {
    position: absolute;
    left: 0; top: 195px;
    width: 283px; height: 316px;
    background: var(--accent-orange);
    border-top-right-radius: 88px;
    color: #fff;
    padding: 42px 26px 0 33px;
    font-size: 10.8px;
    line-height: 12.4px;
  }
  .charges__title { font-size: 13.5px; font-weight: 400; letter-spacing: .3px; margin-bottom: 15px; }
  .charges__list { list-style: none; }
  .charges__list li { display: flex; }
  .charges__list span { flex: 0 0 22px; }
  .charges__note { margin-top: 12px; line-height: 14.8px; }

  /* Front: terms */
  .terms {
    position: absolute;
    left: 323px; top: 24px;
    width: 392px;
    font-size: 10.8px;
    line-height: 12.35px;
  }
  .terms__heading {
    color: var(--heading-orange);
    font-size: 13.5px; font-weight: 700;
    letter-spacing: .2px;
    line-height: 15px;
    margin-top: 13px;
  }
  .terms__heading:first-child { margin-top: 0; }
  .terms__num { display: inline-block; width: 22px; }
  .terms__indent { padding-left: 22px; }
  .terms__row { display: flex; }
  .mark { display: inline-block; width: 22px; flex: 0 0 22px; }
  .terms__gap { height: 12px; }
  .tier { display: flex; padding-left: 22px; }
  .tier__letter { flex: 0 0 70px; font-weight: 700; }
  .tier__name { font-weight: 700; }
  .tier--plain .tier__letter, .tier--plain .tier__name { font-weight: 400; }

  /* Back: policies */
  .policies {
    position: absolute;
    left: 0; top: 0;
    width: 415px; height: 511px;
    background: linear-gradient(160deg, var(--blue-light) 0%, var(--blue-mid) 45%, var(--blue-deep) 100%);
    color: #fff;
    padding: 32px 22px 0 33px;
    font-size: 10.8px;
    line-height: 12.35px;
  }
  .policies__heading {
    font-size: 13.5px; font-weight: 700; letter-spacing: .2px;
    line-height: 15px;
    margin-top: 13px;
  }
  .policies__heading:first-child { margin-top: 0; }
  .policies__num { display: inline-block; width: 22px; }
  .policies__list { list-style: none; }
  .policies__list li { display: flex; }
  .policies__list li::before { content: "•"; flex: 0 0 22px; }
  .policies__closing { margin-top: 13px; }

  /* Back: offer */
  .offer {
    position: absolute;
    left: 415px; top: 0;
    width: 330px; height: 511px;
    padding: 44px 34px 0;
    display: flex; flex-direction: column; align-items: center; text-align: center;
  }
  .offer__brand { display: flex; align-items: center; gap: 8px; }
  .offer__brand .brand__dot { width: 16px; height: 16px; }
  .offer__brand .brand__name { font-size: 22px; }
  .offer__tagline { margin-top: 8px; font-size: 11.5px; color: var(--brand-blue); letter-spacing: .3px; }
  .offer__badge {
    margin-top: 34px;
    width: 100%;
    background: var(--accent-orange);
    color: #fff;
    border-radius: 0 44px 0 0;
    padding: 22px 18px 24px;
  }
  .offer__kicker { font-size: 12.5px; letter-spacing: 1.5px; }
  .offer__amount { font-size: 58px; font-weight: 700; line-height: 1; margin-top: 10px; }
  .offer__detail { font-size: 14px; margin-top: 6px; }
  .offer__extra { font-size: 11.5px; margin-top: 12px; line-height: 1.35; }
  .offer__note { margin-top: 22px; font-size: 11px; line-height: 1.4; color: #333; }
  .offer__rule { width: 60px; height: 2px; background: var(--brand-blue); margin-top: 22px; }
</style>
</head>
<body>

<section class="card card--front">
  <div class="brand">
    <span class="brand__dot"></span>
    <span class="brand__name">Tide Sweepers</span>
  </div>

  <div class="charges">
    <h2 class="charges__title">SERVICE CHARGES</h2>
    <ol class="charges__list">
      <li><span>a)</span>All new Customers are required to have an initial deep filter cleaning and complete equipment inspection.</li>
      <li><span>b)</span>Additional filter cleanings will be performed on a scheduled basis, or as needed, at an additional charge.</li>
      <li><span>c)</span>Replacement cartridges, grids, and other filter parts will be replaced as needed at an additional charge.</li>
      <li><span>d)</span>Any request deemed as service calls, repairs, and evaluations are at an additional charge.</li>
    </ol>
    <p class="charges__note">TIDE SWEEPERS performs filter cleanings to maintain optimal equipment function. These cleanings are charged at time of completion.</p>
  </div>

  <div class="terms">
    <h3 class="terms__heading"><span class="terms__num">1</span>LIABILITY</h3>
    <p class="terms__indent">TIDE SWEEPERS is not liable for pre-existing conditions or equipment failures including but not limited to pumps, motors, filters, or pool structures.</p>

    <h3 class="terms__heading"><span class="terms__num">2.</span>CLIENT RESPONSIBILITIES</h3>
    <p><span class="mark">•</span><b><i>Water Level:</i></b> Clients must maintain proper pool/spa/ fountain water levels. In most cases, the skimmer opening should be submerged halfway underwater. Proper water level ensures effective filtration and chemical balance.</p>
    <div class="terms__gap"></div>
    <p><span class="mark">•</span><b><i>Access &amp; Pool Preparation:</i></b></p>
    <p class="terms__row"><span class="mark">o</span><span>Clear, safe access to the pool area must be provided on the day of service.</span></p>
    <p class="terms__row"><span class="mark">o</span><span>Pool toys, floating mats, and solar covers must be removed prior to service.</span></p>
    <p class="terms__row"><span class="mark">o</span><span>Safety features, including nets or covers, must be removed before our visit. The Company will not remove or reinstall these items.</span></p>
    <p><span class="mark">o</span>Failure to prepare the pool area may result in incomplete service, and no reschedule or credit is guaranteed for such missed services.</p>

    <h3 class="terms__heading"><span class="terms__num">3.</span>SERVICES PROVIDED</h3>
    <p>The Company offers the following service tiers:</p>
    <p class="tier"><span class="tier__letter">a)</span><span class="tier__name">Basic Service</span></p>
    <p class="terms__row"><span class="mark">•</span><span>Two visits per month.</span></p>
    <p><span class="mark">•</span>Diagnostic testing and adjustment for chlorine, pH, and complete water balance.</p>
    <p class="tier tier--plain"><span class="tier__letter">b)</span><span class="tier__name">Basic Plus Service</span></p>
    <p class="terms__row"><span class="mark">•</span><span>Includes Basic Service, plus quarterly filter cleaning and an equipment evaluation.</span></p>
    <p class="tier"><span class="tier__letter">c)</span><span class="tier__name">Full Service</span></p>
    <p class="terms__row"><span class="mark">•</span><span>No less than four visits per month.</span></p>
    <p class="terms__row"><span class="mark">•</span><span>Chemical testing and balance, floating chlorinator maintenance, debris removal, wall and tile brushing, basket emptying, and filter cleaning (for filters under 200 sq. ft).</span></p>
    <p class="tier"><span class="tier__letter">d)</span><span class="tier__name">Extra Full Service</span></p>
    <p class="terms__row"><span class="mark">•</span><span>Recommended for pools prone to heavy debris.</span></p>
    <p class="terms__row"><span class="mark">•</span><span>Includes all Full Service offerings, with six visits per month for weekly cleanings and chemical treatments.</span></p>
  </div>
</section>

<section class="card card--back">
  <div class="policies">
    <h3 class="policies__heading"><span class="policies__num">4.</span>CHEMICALS AND MAINTENANCE</h3>

    <h3 class="policies__heading"><span class="policies__num">5.</span>REPAIRS AND EQUIPMENT MAINTENANCE</h3>
    <ul class="policies__list">
      <li>All repair requests will be evaluated, quoted, and approved by the Client before execution.</li>
      <li>Repairs related to county-mandated safety updates will be billed separately.</li>
    </ul>

    <h3 class="policies__heading"><span class="policies__num">6.</span>WATER CLARITY AND QUALITY GUARANTEE</h3>
    <ul class="policies__list">
      <li>The Company ensures proper chemical balance to prevent algae and bacteria growth.</li>
      <li>Water clarity depends on three factors: chemical balance, filtration, and circulation. The Company guarantees water clarity only as it pertains to chemistry.</li>
    </ul>

    <h3 class="policies__heading"><span class="policies__num">7.</span>EXCLUSIONS</h3>
    <ul class="policies__list">
      <li>Services do not include repairing or addressing structural damage, underground leaks, or equipment not maintained per industry standards.</li>
      <li>Missed visits due to inaccessible areas (e.g., locked gates or unremoved covers) will not be refunded or rescheduled.</li>
    </ul>

    <h3 class="policies__heading"><span class="policies__num">8.</span>ADDITIONAL INFORMATION</h3>
    <ul class="policies__list">
      <li>Safety: Swimming is safe 30 minutes after chemical treatment.</li>
      <li>On-Site Records: Service records will be kept in the pool's timer box and service tags left at the property.</li>
      <li>Initial Start-Up Fee: $85 applies to all new service agreements.</li>
      <li>Service Changes: Service terms and rates are subject to change with 30 days' notice.</li>
    </ul>

    <p class="policies__closing">The service plan includes either 48 or 24 scheduled visits based on a 52-week year, with service pauses during the week of Thanksgiving, Easter, Christmas, and a fourth week at our discretion, with prior notification. Prior to any pause in service, we will take measures to maintain water quality before each scheduled break."</p>
  </div>

  <div class="offer">
    <div class="offer__brand">
      <span class="brand__dot"></span>
      <span class="brand__name">Tide Sweepers</span>
    </div>
    <p class="offer__tagline">Family-owned pool care · San Diego</p>

    <div class="offer__badge">
      <p class="offer__kicker">NEW CUSTOMER SPECIAL</p>
      <p class="offer__amount">$50 OFF</p>
      <p class="offer__detail">your first month of service</p>
      <p class="offer__extra">Plus the $85 start-up fee waived<br>with any monthly service plan.</p>
    </div>

    <div class="offer__rule"></div>
    <p class="offer__note">Mention this card when you book.<br>One offer per household. New residential accounts only.</p>
  </div>
</section>

</body>
</html>
```